Harbor Vantage Web Design Project

We need a website design for a start up company called "Harbor Vantage". We provide business consultancy services as well as technology-related services (IT). The design should communicate simplicity and elegance. The domain name of the site will be harborvantage-example.com. The logo of the company is https://files.example-share.net/u/7418205/4630_2116587_67315_image.jpg

Target Market(s)

SMB, Corporates, Semi-governments, Governments.

Industry/Entity Type

Business

Requirements
Must have
• - The background of the pages should be white or soft grey, but we are open for suggestions.
- The pages should have nice menu animations.
- The pages should be "portal-style", with multiple placeholders for different sections and multiple tabs.
Nice to have
• The page should auto-fit the screen and scroll vertically as much as needed.
Should not have
• - Flash Animations.
- Generic Photos.

```html
<!DOCTYPE html>
<html lang="en">
<head>
<meta charset="utf-8">
<title>Harbor Vantage</title>
<link href="https://fonts.googleapis.com/css2?family=PT+Sans+Narrow:wght@400;700&family=Lato:wght@400&display=swap" rel="stylesheet">
<style>
:root{
  --blue:#1f6db3;
  --red:#d32a2e;
  --red-dark:#a8171c;
  --ink:#3a3a3a;
  --muted:#5b5b5b;
  --line:#e2e2e2;
  --hero-bg:#ececec;
  --footer:#333333;
  --footer-link:#9a9a9a;
}
*{margin:0;padding:0;box-sizing:border-box}
html,body{width:1120px;height:1200px;overflow:hidden;background:#fff}
body{position:relative;font-family:"PT Sans Narrow",sans-serif;color:var(--ink)}
.abs{position:absolute}

/* header */
.site-header{position:absolute;left:0;top:0;width:1120px;height:80px;background:#fff;border-bottom:1px solid #d8d8d8}
.brand{position:absolute;left:166px;top:26px;display:flex;align-items:center;gap:8px;font-size:24px;font-weight:700;color:var(--blue)}
.brand-dot{width:14px;height:14px;border-radius:50%;background:var(--red)}
.main-nav a{position:absolute;top:32px;font-size:13px;letter-spacing:.8px;color:var(--blue);text-decoration:none}
.main-nav a.active{color:var(--red)}

/* hero */
.hero{position:absolute;left:0;top:81px;width:1120px;height:325px;background:radial-gradient(ellipse at 45% 40%,#f7f7f7 0%,#e9e9e9 70%,#e2e2e2 100%);border-bottom:1px solid #d6d6d6}
.hero-shadow{position:absolute;left:130px;top:0;width:860px;height:12px;background:radial-gradient(ellipse at 50% 0,rgba(0,0,0,.22),rgba(0,0,0,0) 70%)}
.hero-title{position:absolute;left:194px;top:56px;font-size:38px;line-height:37px;font-weight:700;letter-spacing:1.6px;color:#555}
.hero-sub{position:absolute;left:195px;top:146px;font-size:16px;font-weight:700;letter-spacing:.6px;color:var(--blue)}
.hero-text{position:absolute;left:195px;top:181px;width:345px;font-size:10px;line-height:14.5px;letter-spacing:.5px;color:var(--muted)}
.btn{position:absolute;display:flex;align-items:center;justify-content:center;font-size:14px;font-weight:700;letter-spacing:1px;color:#7a1013;background:linear-gradient(#e86063,var(--red) 55%,#b91c21);border:1px solid var(--red-dark);border-radius:2px;box-shadow:inset 0 1px 0 rgba(255,255,255,.35)}
.hero-btn{left:195px;top:231px;width:158px;height:31px}
.hero-visual{position:absolute;left:596px;top:42px;width:364px;height:248px;border:2px solid #555;background:linear-gradient(135deg,#dfe6f2 0%,#b9c6dc 45%,#8c9ab3 100%);box-shadow:0 3px 8px rgba(0,0,0,.35)}

/* intro */
.intro{position:absolute;left:160px;top:428px;width:800px;text-align:center;font-size:15px;font-weight:700;letter-spacing:.6px;color:var(--ink)}
.intro span{color:var(--blue)}
.rule{position:absolute;height:1px;background:var(--line)}

/* feature cards */
.card{position:absolute;top:485px;width:187px}
.card-media{width:187px;height:118px}
.card-title{margin-top:21px;padding-left:1px;padding-bottom:5px;font-size:12px;letter-spacing:.4px;color:var(--blue);border-bottom:1px solid var(--line)}
.card-text{margin-top:7px;padding-left:1px;font-size:9.3px;line-height:16px;letter-spacing:.5px;color:var(--muted)}

/* call to action */
.cta{position:absolute;left:160px;top:716px;width:802px;height:69px;border:1px solid #dcdcdc;background:linear-gradient(#fbfbfb,#f3f3f3)}
.cta-title{position:absolute;left:14px;top:13px;font-size:15px;font-weight:700;letter-spacing:.8px;color:var(--ink)}
.cta-text{position:absolute;left:14px;top:36px;font-size:9px;letter-spacing:.6px;color:var(--muted)}
.cta-btn{left:628px;top:17px;width:158px;height:31px}

/* tabs */
.tab{position:absolute;display:flex;align-items:center;justify-content:center;font-family:"Lato",sans-serif;font-size:11px;letter-spacing:2.4px;color:#777;background:linear-gradient(#fafafa,#f0f0f0);border:1px solid #e4e4e4;border-bottom:none}
.tab.active{background:#fff;color:var(--blue);font-size:12.5px;border-top:3px solid #eee}
.tab-panel{position:absolute;left:162px;top:862px;width:798px;height:296px;border:1px solid #e6e6e6;border-bottom:none;background:#fff}
.panel-title{position:absolute;left:19px;top:26px;font-size:18px;font-weight:700;letter-spacing:1.2px;color:var(--ink)}
.panel-text{position:absolute;left:18px;top:67px;width:410px;font-size:10px;line-height:24px;letter-spacing:.35px;color:var(--muted)}
.panel-text em{font-style:normal;color:var(--red)}
.side-title{position:absolute;left:468px;top:74px;font-size:13.5px;font-weight:700;letter-spacing:.6px;color:var(--ink)}
.side-list{position:absolute;left:468px;top:104px;list-style:none}
.side-list li{position:relative;padding-left:16px;height:28.8px;font-size:10px;letter-spacing:.4px;color:var(--blue)}
.side-list li::before{content:"";position:absolute;left:2px;top:3px;border-left:4px solid #444;border-top:3px solid transparent;border-bottom:3px solid transparent}

/* footer */
.site-footer{position:absolute;left:0;top:1158px;width:1120px;height:42px;background:var(--footer)}
.footer-nav a{position:absolute;top:15px;font-size:8.5px;letter-spacing:.4px;color:var(--footer-link);text-decoration:none}
.footer-nav a.active{color:#4c8fd2}
.copyright{position:absolute;right:160px;top:15px;font-size:8.5px;letter-spacing:.4px;color:var(--footer-link)}
</style>
</head>
<body>

<header class="site-header">
  <div class="brand"><span class="brand-dot"></span>Harbor Vantage</div>
  <nav class="main-nav">
    <a class="active" href="#" style="left:540px">home</a>
    <a href="#" style="left:635px">about</a>
    <a href="#" style="left:713px">work</a>
    <a href="#" style="left:785px">blog</a>
    <a href="#" style="left:856px">faq</a>
    <a href="#" style="left:921px">contact</a>
  </nav>
</header>

<section class="hero">
  <div class="hero-shadow"></div>
  <h1 class="hero-title">Phasellus alimueter<br>fementum eros allen</h1>
  <p class="hero-sub">Nelementum velit erting toning ellening tarbons</p>
  <p class="hero-text">Lorem ipsum dolor sit amet, consectetur adipiscing elit. Nulla blandit ante at risus auctor aliquam non non eroson. Vestibulum pretiuming terney geretable</p>
  <a class="btn hero-btn">Get Started</a>
  <div class="hero-visual" role="img" aria-label="Browser window showing a hand pointing at business charts on a monitor"></div>
</section>

<h2 class="intro">Donec fringilla, massa sit amet auctor tristique, velit lectus <span>elementum velit erting toning</span></h2>
<div class="rule" style="left:160px;top:467px;width:800px"></div>

<article class="card" style="left:162px">
  <div class="card-media" role="img" aria-label="Hand pointing at charts on a monitor" style="background:linear-gradient(135deg,#eef0f4,#b9c3d3 60%,#d8dce4)"></div>
  <h3 class="card-title">Donec fringilla</h3>
  <p class="card-text">Lorem ipsum dolor sit amet, consectetur adipiscing elit. Nulla blandit ante at risus</p>
</article>
<article class="card" style="left:365px">
  <div class="card-media" role="img" aria-label="Person with a coffee cup and a tablet holding a card" style="background:linear-gradient(160deg,#c7d8ee,#9fb8da 50%,#c7a17e 80%,#f2f2f2)"></div>
  <h3 class="card-title">Donec fringilla</h3>
  <p class="card-text">Lorem ipsum dolor sit amet, consectetur adipiscing elit. Nulla blandit ante at risus</p>
</article>
<article class="card" style="left:569px">
  <div class="card-media" role="img" aria-label="Businesswoman working at a laptop in an office" style="background:linear-gradient(120deg,#9aa9b8,#3f4a57 40%,#c8b49a 70%,#7b8ea3)"></div>
  <h3 class="card-title">Donec fringilla</h3>
  <p class="card-text">Lorem ipsum dolor sit amet, consectetur adipiscing elit. Nulla blandit ante at risus</p>
</article>
<article class="card" style="left:773px">
  <div class="card-media" role="img" aria-label="Hand on a computer mouse beside a keyboard" style="background:linear-gradient(135deg,#f3f3f3,#e0c0ad 45%,#3a3d44 70%,#e8ecef)"></div>
  <h3 class="card-title">Donec fringilla</h3>
  <p class="card-text">Lorem ipsum dolor sit amet, consectetur adipiscing elit. Nulla blandit ante at risus</p>
</article>

<aside class="cta">
  <h2 class="cta-title">Mauris rutrum ante mattis neque pellentesque</h2>
  <p class="cta-text">Integer rutrum nunc eu dui rutrum vel cursus purus fermentum. Duis mattis odio id erat vestibulum bibendum elenrotte eke</p>
  <a class="btn cta-btn">Get Started</a>
</aside>

<div class="tab active" style="left:162px;top:813px;width:223px;height:50px">Tab Heading</div>
<div class="tab" style="left:385px;top:826px;width:191px;height:36px">Tab Heading</div>
<div class="tab" style="left:576px;top:826px;width:192px;height:36px">Tab Heading</div>
<div class="tab" style="left:768px;top:826px;width:192px;height:36px">Tab Heading</div>

<section class="tab-panel">
  <h2 class="panel-title">Phasellus aliquet fermentum eros allen</h2>
  <div class="rule" style="left:19px;top:56px;width:726px"></div>
  <p class="panel-text">Lorem ipsum dolor sit amet, consectetur adipiscing elit. Nulla blandit ante at risus auctor aliquam non non eroson. Vestibulum pretium <em>blandit nisl in</em> laoreet. Suspendisse ut auctor diam. Vestibulum gravida adipiscing leo, non <em>tempus quam</em> scelerisque annelre gingelrty edertserbii ellerting yun iouksble.<br>Vestibulum pretium <em>blandit nisl in</em> laoreet. Suspendisse ut auctor diam. Vestibulum gravida adipiscing leo, non tempus quam scelerisque a.</p>
  <h3 class="side-title">Lorem ipsum deler</h3>
  <ul class="side-list">
    <li>Lorem ipsum dolor sit amet, consectetur adipiscing</li>
    <li>Nulla blandit ante at risus auctor aliquam non non</li>
    <li>Lorem ipsum dolor sit amet, consectetur adipiscing</li>
    <li>Nulla blandit ante at risus auctor aliquam eroson</li>
  </ul>
</section>

<footer class="site-footer">
  <nav class="footer-nav">
    <a class="active" href="#" style="left:159px">Home</a>
    <a href="#" style="left:208px">Services</a>
    <a href="#" style="left:267px">Blog</a>
    <a href="#" style="left:311px">Guarantee</a>
    <a href="#" style="left:374px">Contact</a>
  </nav>
  <p class="copyright">Copyright © 2012 | All rights reserved</p>
</footer>

</body>
</html>
```